GHollis Busisness Card

I am an aerospace consultant and at this time only need business cards.

Industry/Entity Type

Business

Contact Information for Business Card

Hollis Partners,LLC
Gerald T. Hollis

348 Birch Hollow Road
Madison AL 35762

256-555-0148 (cell)
256-555-0173 (fax)

geraldhollis@mailbrook.net

```html
<!DOCTYPE html>
<html lang="en">
<head>
<meta charset="utf-8">
<title>Hollis Partners, LLC — Business Card</title>
<link rel="stylesheet" href="https://fonts.googleapis.com/css2?family=Open+Sans:wght@400;600&display=swap">
<style>
  :root {
    --page-bg: #e9e9ec;
    --card-bg: #ffffff;
    --brand-blue: #2f4b9e;
    --brand-blue-light: #4f7ad0;
    --name-blue: #2c3f86;
    --ink: #1c1c1c;
    --icon-ink: #2c3f86;
    --edge-blue: #2f4b9e;
  }
  * { margin: 0; padding: 0; box-sizing: border-box; }
  html, body {
    width: 1200px;
    height: 800px;
    overflow: hidden;
    background: var(--page-bg);
    font-family: "Open Sans", Arial, sans-serif;
  }
  .card {
    position: absolute;
    left: 180px;
    top: 160px;
    width: 840px;
    height: 480px;
    background: var(--card-bg);
    border-bottom: 6px solid var(--edge-blue);
    box-shadow: 0 8px 24px rgba(0,0,0,0.18);
  }
  .brand {
    position: absolute;
    left: 60px;
    top: 60px;
    display: flex;
    align-items: center;
    gap: 26px;
  }
  .brand-square {
    width: 150px;
    height: 150px;
    border-radius: 18px;
    background: var(--brand-blue);
  }
  .brand-name {
    font-size: 44px;
    font-weight: 400;
    color: var(--ink);
    letter-spacing: 0.5px;
    margin-top: -70px;
  }
  .person-name {
    position: absolute;
    left: 60px;
    top: 262px;
    font-size: 30px;
    font-weight: 600;
    color: var(--name-blue);
  }
  .contact-list {
    position: absolute;
    left: 60px;
    top: 314px;
    list-style: none;
  }
  .contact-item {
    display: flex;
    align-items: center;
    gap: 10px;
    height: 36px;
    font-size: 25px;
    color: var(--ink);
  }
  .contact-icon {
    width: 26px;
    height: 26px;
    flex: none;
  }
</style>
</head>
<body>
  <main class="card">
    <div class="brand">
      <div class="brand-square"></div>
      <div class="brand-name">Hollis Partners,LLC</div>
    </div>

    <h1 class="person-name">Gerald T. Hollis</h1>

    <ul class="contact-list">
      <li class="contact-item">
        <svg class="contact-icon" viewBox="0 0 26 26" aria-hidden="true">
          <rect x="6" y="2" width="14" height="22" rx="2" fill="var(--icon-ink)"/>
          <rect x="8.5" y="5" width="9" height="8" fill="#fff"/>
          <circle cx="10" cy="16.5" r="1" fill="#fff"/><circle cx="13" cy="16.5" r="1" fill="#fff"/><circle cx="16" cy="16.5" r="1" fill="#fff"/>
          <circle cx="10" cy="20" r="1" fill="#fff"/><circle cx="13" cy="20" r="1" fill="#fff"/><circle cx="16" cy="20" r="1" fill="#fff"/>
        </svg>
        <span>256-555-0148</span>
      </li>
      <li class="contact-item">
        <svg class="contact-icon" viewBox="0 0 26 26" aria-hidden="true">
          <rect x="7" y="2" width="12" height="8" fill="none" stroke="var(--icon-ink)" stroke-width="2"/>
          <rect x="2" y="9" width="22" height="11" rx="2" fill="var(--icon-ink)"/>
          <rect x="7" y="16" width="12" height="8" fill="#fff" stroke="var(--icon-ink)" stroke-width="2"/>
        </svg>
        <span>256-555-0173</span>
      </li>
      <li class="contact-item">
        <svg class="contact-icon" viewBox="0 0 26 26" aria-hidden="true">
          <rect x="2" y="6" width="22" height="15" rx="2" fill="var(--icon-ink)"/>
          <path d="M3 7 L13 15 L23 7" fill="none" stroke="#fff" stroke-width="2"/>
        </svg>
        <span>geraldhollis@mailbrook.net</span>
      </li>
      <li class="contact-item">
        <svg class="contact-icon" viewBox="0 0 26 26" aria-hidden="true">
          <path d="M2 13 L13 3 L24 13" fill="none" stroke="var(--icon-ink)" stroke-width="2.5" stroke-linejoin="round"/>
          <path d="M6 12 V23 H11 V17 H15 V23 H20 V12 L13 6 Z" fill="var(--icon-ink)"/>
        </svg>
        <span>348 Birch Hollow Road Madison AL 35762</span>
      </li>
    </ul>
  </main>
</body>
</html>
```